Custom beer tap decals, Halvett Brewery, Tasmania, Australia.

UPDATE 22/6/2017

Based on designs received so far, Im after more of a bold/clean design. This must standout. See attached example.

Beer tap decals for 4 different products. Rustic/English feel, with some modern vibrancy, maintain original branding as much as possible.
The size bust be a 95mm circle. Please see attached artwork.
The same branding theme must carry across all four designs. While each can be different, the core branding remaining the same is important.
Happy for different fonts to be used, but they must be clearly readable. The font for the 'Halvett Brewery' component must remain the same.
The colours used in the flag banner part of the decal must remain the same as these reflect the colours on our bottle labels.

Highlighting the 'Made in Tasmania' component would be nice, although not entirely necessary.

Plus a 'Limited Release; design including white space where one off beers can be written in permanent marker, we brew quite a few small batch beers per year and it doesn’t make sense to have custom decals for each. Having a generic limited release decal that we can change ourselves would be a big help.

Target Market(s)

Graphic design, beer, brewery.

Industry/Entity Type

Brewery

Colors

Designer to choose colors to be used in the design.

Requirements
Must have
• 'Halvett Brewery' component of supplied decals must remain. Would be nice to incorporate some of the shield elements, but isn't vital.
Nice to have
• Rustic/earth themes, with a modern twist and vibrance.

```html
<!DOCTYPE html>
<html lang="en">
<head>
<meta charset="utf-8">
<title>Halvett Brewery – Tap Decals</title>
<link rel="stylesheet" href="https://fonts.googleapis.com/css2?family=Cinzel:wght@400;700;900&display=swap">
<style>
  :root {
    --ring-green: #1f6b34;
    --disc-black: #000000;
    --shield-beige: #d5cc94;
    --ink: #111111;
    --hop-light: #8fd14f;
    --hop-dark: #2f8a2c;
    --band-red-ale: #a52f38;
    --band-stout: #eceacb;
    --band-bitter: #c9a149;
    --band-pale-ale: #ef8a3a;
    --band-limited: #ffffff;
    --page: #ffffff;
  }
  html, body {
    margin: 0;
    padding: 0;
    overflow: hidden;
    background: var(--page);
  }
  .sheet {
    position: relative;
    width: 848px;
    height: 1200px;
    overflow: hidden;
    background: var(--page);
  }
  .decal {
    position: absolute;
    width: 384px;
    height: 384px;
  }
  .decal--red-ale   { left: 24px;  top: 24px; }
  .decal--stout     { left: 440px; top: 24px; }
  .decal--bitter    { left: 24px;  top: 424px; }
  .decal--pale-ale  { left: 440px; top: 424px; }
  .decal--limited   { left: 232px; top: 792px; }

  .ring   { fill: var(--ring-green); }
  .disc   { fill: var(--disc-black); }
  .shield { fill: var(--shield-beige); stroke: var(--ring-green); stroke-width: 9; stroke-linejoin: round; }
  .band-rule { stroke: var(--ink); stroke-width: 2.5; }
  .hop-art { fill: url(#hopTone); }

  .brand-name {
    font-family: "Cinzel", serif;
    font-weight: 700;
    font-size: 58px;
    fill: var(--ink);
    letter-spacing: 1px;
  }
  .brand-sub {
    font-family: "Cinzel", serif;
    font-weight: 700;
    font-size: 24px;
    fill: var(--ink);
    letter-spacing: 1px;
  }
  .beer-name {
    font-family: "Cinzel", serif;
    font-weight: 900;
    font-size: 31px;
    fill: var(--ink);
  }
  .beer-name--large { font-size: 40px; }
  .origin-line {
    font-family: "Cinzel", serif;
    font-weight: 700;
    font-size: 12.5px;
    fill: var(--ink);
  }
  .abv {
    font-family: "Cinzel", serif;
    font-weight: 700;
    font-size: 15px;
    fill: var(--ink);
  }
  .edition-label {
    font-family: "Cinzel", serif;
    font-weight: 700;
    font-size: 17px;
    fill: #ffffff;
    letter-spacing: 1px;
  }
</style>
</head>
<body>
<main class="sheet">

  <svg width="0" height="0" style="position:absolute" aria-hidden="true">
    <defs>
      <radialGradient id="hopTone" cx="50%" cy="55%" r="60%">
        <stop offset="0%" stop-color="#a6db5a"/>
        <stop offset="60%" stop-color="#4aa33a"/>
        <stop offset="100%" stop-color="#2a7a2a"/>
      </radialGradient>
      <clipPath id="shieldClip">
        <path d="M30,172 Q240,112 450,172 L382,392 Q320,430 240,458 Q160,430 98,392 Z"/>
      </clipPath>
      <path id="editionArc" d="M70,240 A170,170 0 0 1 410,240"/>
    </defs>
  </svg>

  <!-- Irish Red Ale -->
  <svg class="decal decal--red-ale" viewBox="0 0 480 480">
    <circle class="ring" cx="240" cy="240" r="240"/>
    <circle class="disc" cx="240" cy="240" r="228"/>
    <path d="M80,150 A190,190 0 0 1 400,150" fill="none" stroke="var(--band-red-ale)" stroke-width="3"/>
    <path class="shield" d="M30,172 Q240,112 450,172 L382,392 Q320,430 240,458 Q160,430 98,392 Z"/>
    <g clip-path="url(#shieldClip)">
      <rect x="0" y="266" width="480" height="70" fill="var(--band-red-ale)"/>
      <line class="band-rule" x1="0" y1="266" x2="480" y2="266"/>
      <line class="band-rule" x1="0" y1="336" x2="480" y2="336"/>
    </g>
    <ellipse class="hop-art" cx="240" cy="100" rx="100" ry="70" role="img" aria-label="Hop cones and leaves illustration"/>
    <text class="brand-name" x="240" y="220" text-anchor="middle">HALVETT</text>
    <text class="brand-sub" x="240" y="250" text-anchor="middle">BREWERY</text>
    <text class="beer-name" x="240" y="312" text-anchor="middle">IRISH RED ALE</text>
    <text class="origin-line" x="240" y="362" text-anchor="middle">PROUDLY</text>
    <text class="origin-line" x="240" y="378" text-anchor="middle">TASMANIAN MADE</text>
    <text class="abv" x="240" y="410" text-anchor="middle">5.1%</text>
  </svg>

  <!-- Irish Stout -->
  <svg class="decal decal--stout" viewBox="0 0 480 480">
    <circle class="ring" cx="240" cy="240" r="240"/>
    <circle class="disc" cx="240" cy="240" r="228"/>
    <path d="M80,150 A190,190 0 0 1 400,150" fill="none" stroke="var(--band-stout)" stroke-width="3"/>
    <path class="shield" d="M30,172 Q240,112 450,172 L382,392 Q320,430 240,458 Q160,430 98,392 Z"/>
    <g clip-path="url(#shieldClip)">
      <rect x="0" y="262" width="480" height="76" fill="var(--band-stout)"/>
      <line class="band-rule" x1="0" y1="262" x2="480" y2="262"/>
      <line class="band-rule" x1="0" y1="338" x2="480" y2="338"/>
    </g>
    <ellipse class="hop-art" cx="240" cy="100" rx="100" ry="70" role="img" aria-label="Hop cones and leaves illustration"/>
    <text class="brand-name" x="240" y="218" text-anchor="middle">HALVETT</text>
    <text class="brand-sub" x="240" y="248" text-anchor="middle">BREWERY</text>
    <text class="beer-name" x="240" y="311" text-anchor="middle">IRISH STOUT</text>
    <text class="origin-line" x="240" y="360" text-anchor="middle">PROUDLY</text>
    <text class="origin-line" x="240" y="376" text-anchor="middle">TASMANIAN MADE</text>
    <text class="abv" x="240" y="408" text-anchor="middle">4.7%</text>
  </svg>

  <!-- English Bitter -->
  <svg class="decal decal--bitter" viewBox="0 0 480 480">
    <circle class="ring" cx="240" cy="240" r="240"/>
    <circle class="disc" cx="240" cy="240" r="228"/>
    <path d="M80,150 A190,190 0 0 1 400,150" fill="none" stroke="var(--band-bitter)" stroke-width="3"/>
    <path class="shield" d="M30,172 Q240,112 450,172 L382,392 Q320,430 240,458 Q160,430 98,392 Z"/>
    <g clip-path="url(#shieldClip)">
      <rect x="0" y="264" width="480" height="72" fill="var(--band-bitter)"/>
      <line class="band-rule" x1="0" y1="264" x2="480" y2="264"/>
      <line class="band-rule" x1="0" y1="336" x2="480" y2="336"/>
    </g>
    <ellipse class="hop-art" cx="240" cy="100" rx="100" ry="70" role="img" aria-label="Hop cones and leaves illustration"/>
    <text class="brand-name" x="240" y="220" text-anchor="middle">HALVETT</text>
    <text class="brand-sub" x="240" y="250" text-anchor="middle">BREWERY</text>
    <text class="beer-name" x="240" y="311" text-anchor="middle" textLength="340" lengthAdjust="spacingAndGlyphs">ENGLISH BITTER</text>
    <text class="origin-line" x="240" y="360" text-anchor="middle">PROUDLY</text>
    <text class="origin-line" x="240" y="376" text-anchor="middle">TASMANIAN MADE</text>
    <text class="abv" x="240" y="410" text-anchor="middle">4.2%</text>
  </svg>

  <!-- Pale Ale -->
  <svg class="decal decal--pale-ale" viewBox="0 0 480 480">
    <circle class="ring" cx="240" cy="240" r="240"/>
    <circle class="disc" cx="240" cy="240" r="228"/>
    <path d="M80,150 A190,190 0 0 1 400,150" fill="none" stroke="var(--band-pale-ale)" stroke-width="3"/>
    <path class="shield" d="M30,172 Q240,112 450,172 L382,392 Q320,430 240,458 Q160,430 98,392 Z"/>
    <g clip-path="url(#shieldClip)">
      <rect x="0" y="264" width="480" height="72" fill="var(--band-pale-ale)"/>
      <line class="band-rule" x1="0" y1="264" x2="480" y2="264"/>
      <line class="band-rule" x1="0" y1="336" x2="480" y2="336"/>
    </g>
    <ellipse class="hop-art" cx="240" cy="100" rx="100" ry="70" role="img" aria-label="Hop cones and leaves illustration"/>
    <text class="brand-name" x="240" y="220" text-anchor="middle">HALVETT</text>
    <text class="brand-sub" x="240" y="250" text-anchor="middle">BREWERY</text>
    <text class="beer-name beer-name--large" x="240" y="315" text-anchor="middle">PALE ALE</text>
    <text class="origin-line" x="240" y="360" text-anchor="middle">PROUDLY</text>
    <text class="origin-line" x="240" y="376" text-anchor="middle">TASMANIAN MADE</text>
    <text class="abv" x="240" y="410" text-anchor="middle">4.2%</text>
  </svg>

  <!-- Limited Edition -->
  <svg class="decal decal--limited" viewBox="0 0 480 480">
    <circle class="ring" cx="240" cy="240" r="240"/>
    <circle class="disc" cx="240" cy="240" r="228"/>
    <text class="edition-label" text-anchor="middle">
      <textPath href="#editionArc" startOffset="50%">LIMITED&#160;&#160;&#160;&#160;&#160;&#160;&#160;&#160;&#160;&#160;&#160;EDITION</textPath>
    </text>
    <path d="M80,150 A190,190 0 0 1 400,150" fill="none" stroke="var(--band-limited)" stroke-width="3"/>
    <path class="shield" d="M30,172 Q240,112 450,172 L382,392 Q320,430 240,458 Q160,430 98,392 Z"/>
    <g clip-path="url(#shieldClip)">
      <rect x="0" y="262" width="480" height="96" fill="var(--band-limited)"/>
      <line class="band-rule" x1="0" y1="262" x2="480" y2="262"/>
      <line class="band-rule" x1="0" y1="358" x2="480" y2="358"/>
    </g>
    <ellipse class="hop-art" cx="240" cy="100" rx="100" ry="70" role="img" aria-label="Hop cones and leaves illustration"/>
    <text class="brand-name" x="240" y="220" text-anchor="middle">HALVETT</text>
    <text class="brand-sub" x="240" y="250" text-anchor="middle">BREWERY</text>
    <text class="origin-line" x="240" y="388" text-anchor="middle">PROUDLY</text>
    <text class="origin-line" x="240" y="404" text-anchor="middle">TASMANIAN MADE</text>
  </svg>

</main>
</body>
</html>
```